Real Estate Wordpress Landing Page

I'm looking to a landing page dedicated to my real estate brokerage that's catered to promoting that my company provides 1.5% listings to home sellers... I have a couple examples that I'm really looking towards mocking in a version with similar color schemes using my current company colors/website.

http://halvorik.com/
https://www.brambelo.com/about/one-percent-listing-fee

My brokerage company website is http://www.clearmarrow.us/

Target Market(s)

real estate home sellers & buyers

Industry/Entity Type

Real Estate

Coding

Coded - Design and coding required

Number of Pages Required

1 page

Colors
3176b5
0255a3
eaf1f7
cedeed

Requirements
Must have
• Company website colors - http://www.clearmarrow.us/
• Something around the lines of this website page - http://halvorik.com/
• Wordpress compatibility

```html
<!DOCTYPE html>
<html lang="en">
<head>
<meta charset="utf-8">
<title>Clearmarrow – List for 1.5% Commission</title>
<link href="https://fonts.googleapis.com/css2?family=Open+Sans:wght@400;600;700&family=Montserrat:wght@400;500;600;700&family=Courgette&display=swap" rel="stylesheet">
<style>
:root{
  --blue:#0255a3;
  --blue-mid:#3176b5;
  --ice:#eaf1f7;
  --mist:#cedeed;
  --orange:#f7941d;
  --ink:#2b2b2b;
  --grey:#777;
  --line:#e2e2e2;
  --dark:#1c1c1c;
}
*{box-sizing:border-box;margin:0;padding:0}
html,body{width:1200px;height:3838px;overflow:hidden;background:#fff}
body{font-family:"Open Sans",Arial,sans-serif;color:var(--ink);position:relative}
.page{position:relative;width:1200px;height:3838px;overflow:hidden}
.abs{position:absolute}
.btn{position:absolute;background:var(--orange);color:#fff;font-family:"Montserrat",sans-serif;font-weight:700;font-size:17px;display:flex;align-items:center;justify-content:center;letter-spacing:.5px;border-radius:2px}

/* top bar */
.topbar{position:absolute;left:0;top:0;width:1200px;height:102px;background:#fff}
.infostrip{position:absolute;left:0;top:0;width:1200px;height:22px;background:var(--blue);color:#fff;font-size:11px;display:flex;align-items:center;padding-left:143px;gap:28px}
.infostrip span{display:flex;align-items:center;gap:6px}
.infostrip .socials{margin-left:auto;margin-right:143px;display:flex;gap:10px}
.dot{width:10px;height:10px;border-radius:50%;background:#fff;display:inline-block}
.brand{position:absolute;left:143px;top:40px;display:flex;align-items:center;gap:10px}
.brand-mark{width:34px;height:34px;background:var(--blue)}
.brand-name{font-family:"Montserrat",sans-serif;font-weight:700;font-size:22px;color:var(--blue)}
.contacts{position:absolute;right:143px;top:56px;display:flex;gap:40px;font-size:15px;color:var(--ink)}
.contacts span{display:flex;align-items:center;gap:10px}

/* hero */
.hero{position:absolute;left:0;top:102px;width:1200px;height:600px;background:linear-gradient(180deg,#9fb6c6 0%,#c9cfc6 30%,#6f8a4d 62%,#4f7a2e 100%)}
.hero-title{position:absolute;left:143px;top:318px;color:#fff;font-family:"Montserrat",sans-serif;font-weight:700;font-size:38px;text-shadow:0 2px 6px rgba(0,0,0,.35)}
.hero-sub{position:absolute;left:143px;top:368px;color:#fff;font-size:17px;text-shadow:0 1px 4px rgba(0,0,0,.4)}
.search{position:absolute;left:742px;top:181px;width:317px;height:387px;background:#fff;box-shadow:0 4px 16px rgba(0,0,0,.2)}
.search-head{height:34px;background:var(--blue);color:#fff;font-family:"Montserrat",sans-serif;font-weight:700;font-size:15px;display:flex;align-items:center;justify-content:center}
.search-body{padding:12px 30px}
.field-label{font-size:11px;color:#444;margin-top:10px;margin-bottom:4px}
.field{height:26px;border:1px solid var(--line);font-size:10px;color:#999;display:flex;align-items:center;justify-content:space-between;padding:0 8px}
.row{display:flex;gap:16px}.row>div{flex:1}
.search-btn{margin-top:18px;height:30px;background:var(--blue);color:#fff;font-size:12px;display:flex;align-items:center;justify-content:center;font-weight:600}

/* service band */
.service-band{position:absolute;left:0;top:670px;width:1200px;height:243px;background:linear-gradient(180deg,var(--blue) 0%,#0a4f95 70%,#1b5f9f 100%)}
.service{position:absolute;width:240px;text-align:center;color:#fff;font-family:"Montserrat",sans-serif;font-weight:600;font-size:14px;line-height:20px}
.service .circle{width:120px;height:120px;border-radius:50%;background:var(--blue);border:4px solid #fff;margin:0 auto 14px;display:flex;align-items:center;justify-content:center}

/* section titles */
.sec-title{position:absolute;left:0;width:1200px;text-align:center;font-family:"Montserrat",sans-serif;font-size:30px;font-weight:400;color:#888;letter-spacing:.5px}
.sec-title b{color:var(--blue);font-weight:600}

/* property cards */
.prop{position:absolute;top:1069px;width:290px;height:320px;border-radius:4px;overflow:hidden}
.prop .photo{position:absolute;inset:0}
.badge{position:absolute;top:24px;right:0;background:var(--orange);color:#fff;font-size:14px;font-weight:600;padding:6px 12px}
.prop .addr{position:absolute;left:0;right:0;bottom:18px;text-align:center;color:#fff;font-weight:700;font-size:15px;line-height:21px;text-shadow:0 1px 4px rgba(0,0,0,.6)}

/* realtor band */
.realtor-band{position:absolute;left:0;top:1543px;width:1200px;height:215px;background:var(--blue-mid)}
.realtor-frame{position:absolute;left:143px;top:30px;width:914px;height:167px;border:1px solid rgba(255,255,255,.6);text-align:center;color:#fff}
.realtor-frame h2{font-family:"Courgette",cursive;font-weight:400;font-size:20px;margin-top:14px}
.realtor-frame p{font-size:13px;line-height:20px;margin:10px auto 0;width:700px}

/* sold */
.sold{position:absolute;top:1909px;width:218px;height:240px;background:#222;border-radius:3px;overflow:hidden}
.sold .photo{position:absolute;left:0;top:0;width:218px;height:202px}
.sold .tag{position:absolute;top:26px;right:6px;background:var(--orange);color:#fff;font-size:12px;font-weight:700;padding:4px 9px}
.sold .info{position:absolute;left:0;right:0;top:148px;text-align:center;color:#fff;font-size:12px;line-height:18px;text-shadow:0 1px 3px rgba(0,0,0,.7)}
.sold .info b{color:var(--orange);font-size:14px}
.sold .meta{position:absolute;left:0;right:0;bottom:0;height:38px;display:flex;justify-content:space-around;align-items:center;color:#ddd;font-size:11px}
.arrow{position:absolute;top:2015px;color:#bbb;font-size:24px}

/* broker */
.broker{position:absolute;left:0;top:2221px;width:1200px;height:465px;background:linear-gradient(90deg,#fff 0%,#f6f6f6 50%,#e4e4e4 100%)}
.broker-photo{position:absolute;left:700px;top:90px;width:362px;height:375px;background:linear-gradient(180deg,#d5d5d5,#5a5a5a)}
.broker-name{position:absolute;left:143px;top:112px;font-family:"Courgette",cursive;font-size:30px;color:#222}
.broker-text{position:absolute;left:143px;top:172px;width:560px;font-size:16px;line-height:26px;color:#333}
.broker-text b{color:var(--blue)}
.broker-call{position:absolute;left:143px;top:250px;font-family:"Montserrat",sans-serif;font-weight:700;font-size:20px;color:var(--blue)}
.broker-web{position:absolute;left:143px;top:296px;font-size:14px;font-weight:600;display:flex;align-items:center;gap:8px}
.follow{position:absolute;left:143px;top:336px;font-size:14px;display:flex;align-items:center;gap:8px}
.social-c{width:26px;height:26px;border-radius:50%;background:var(--blue)}

/* testimonials */
.testi{position:absolute;top:2835px;width:281px;height:177px;border:1px solid var(--line);background:#fff;padding:24px 20px}
.testi .avatar{position:absolute;left:20px;top:24px;width:46px;height:46px;border-radius:50%;background:linear-gradient(180deg,var(--mist),#9bb3c9)}
.testi .who{margin-left:64px;font-weight:700;font-size:13px}
.testi .stars{margin-left:64px;margin-top:4px;color:#bbb;font-size:13px;letter-spacing:2px}
.testi p{margin-left:64px;margin-top:8px;font-size:11px;line-height:16px;color:#555}
.dots{position:absolute;top:3050px;left:570px;display:flex;gap:6px}
.dots i{display:block;width:20px;height:4px;background:var(--mist)}
.dots i:first-child{background:var(--blue)}

/* cta */
.cta{position:absolute;left:0;top:3134px;width:1200px;height:174px;background:linear-gradient(90deg,var(--blue) 0%,var(--blue-mid) 60%,#8fb0d2 100%)}
.cta-photo{position:absolute;left:742px;top:0;width:458px;height:174px;background:linear-gradient(90deg,rgba(234,241,247,0),#dfe6ee 25%,#b6c4d3 100%)}
.cta h3{position:absolute;left:143px;top:26px;color:#fff;font-family:"Montserrat",sans-serif;font-weight:700;font-size:29px}
.cta h4{position:absolute;left:143px;top:66px;color:var(--orange);font-family:"Montserrat",sans-serif;font-weight:700;font-size:29px}
.cta h5{position:absolute;left:143px;top:114px;color:#fff;font-family:"Montserrat",sans-serif;font-weight:700;font-size:20px}

/* contact */
.contact{position:absolute;left:0;top:3308px;width:1200px;height:484px;background:linear-gradient(180deg,#f1f1f1,#e6e8ea)}
.kicker{position:absolute;font-size:11px;color:#444;letter-spacing:.3px}
.contact h2{position:absolute;font-family:"Montserrat",sans-serif;font-weight:500;font-size:28px;color:var(--blue)}
.input{position:absolute;left:200px;width:322px;height:30px;background:#fff;font-size:11px;color:#999;padding:0 14px;display:flex;align-items:center}
.send{position:absolute;left:200px;top:378px;width:322px;height:30px;background:var(--blue);color:#fff;font-size:12px;font-weight:600;display:flex;align-items:center;justify-content:center}
.office{position:absolute;left:727px;width:330px;display:flex;gap:20px}
.office .ic{width:34px;height:34px;border-radius:50%;background:var(--blue);flex:none;display:flex;align-items:center;justify-content:center}
.office .t{font-size:12px;line-height:18px;color:#333}
.office .t b{display:block;font-size:12px}

.footer{position:absolute;left:0;top:3792px;width:1200px;height:46px;background:var(--dark);color:#ccc;font-size:12px;display:flex;align-items:center;padding:0 143px}
.footer .socials{margin-left:auto;display:flex;gap:8px}
.footer .socials i{display:block;width:24px;height:24px;border-radius:50%;background:#fff}
</style>
</head>
<body>
<div class="page">

  <header class="topbar">
    <div class="infostrip">
      <span><svg width="9" height="12" viewBox="0 0 9 12"><path d="M4.5 0A4.5 4.5 0 0 0 0 4.5C0 8 4.5 12 4.5 12S9 8 9 4.5A4.5 4.5 0 0 0 4.5 0zm0 6.3a1.8 1.8 0 1 1 0-3.6 1.8 1.8 0 0 1 0 3.6z" fill="#fff"/></svg>2140 Harbor Crest Blvd, Ste 310 Boynton Beach, FL 33426</span>
      <span><svg width="11" height="11" viewBox="0 0 12 12"><circle cx="6" cy="6" r="5" fill="none" stroke="#fff" stroke-width="1.4"/><path d="M6 3v3l2 1.5" stroke="#fff" stroke-width="1.4" fill="none"/></svg>9 am to 5 pm monday To Friday</span>
      <span class="socials"><i class="dot"></i><i class="dot"></i><i class="dot"></i><i class="dot"></i><i class="dot"></i></span>
    </div>
    <div class="brand"><div class="brand-mark"></div><div class="brand-name">Clearmarrow</div></div>
    <div class="contacts">
      <span><svg width="18" height="18" viewBox="0 0 24 24"><path d="M6.6 10.8a15 15 0 0 0 6.6 6.6l2.2-2.2c.3-.3.7-.4 1-.2 1.1.4 2.3.6 3.6.6.6 0 1 .4 1 1V20c0 .6-.4 1-1 1A17 17 0 0 1 3 4c0-.6.4-1 1-1h3.5c.6 0 1 .4 1 1 0 1.3.2 2.5.6 3.6.1.3 0 .7-.2 1z" fill="var(--blue)"/></svg>561-555-0184</span>
      <span><svg width="20" height="16" viewBox="0 0 20 16"><rect x="1" y="1" width="18" height="14" rx="1" fill="none" stroke="var(--blue)" stroke-width="1.6"/><path d="M1 2l9 7 9-7" fill="none" stroke="var(--blue)" stroke-width="1.6"/></svg>contact@clearmarrow.us</span>
    </div>
  </header>

  <section class="hero" role="img" aria-label="Photo of a single-storey Florida home with palm trees and a green front lawn">
  </section>
  <h1 class="hero-title abs">LIST FOR 1.5% COMMISSION,</h1>
  <p class="hero-sub">And Receive Top Marketing from Real Estate Pro!</p>
  <div class="btn" style="left:143px;top:421px;width:212px;height:38px">CONTACT US TODAY</div>

  <form class="search">
    <div class="search-head">SEARCH PROPERTIES</div>
    <div class="search-body">
      <div class="field-label">Location</div>
      <div class="field">Enter City or Zip<span>▾</span></div>
      <div class="field-label">Property Type</div>
      <div class="field">House / Condo<span>▾</span></div>
      <div class="row">
        <div><div class="field-label">Min. Price</div><div class="field">$<span>No min</span></div></div>
        <div><div class="field-label">Max. Price</div><div class="field">$<span>No max</span></div></div>
      </div>
      <div class="row">
        <div><div class="field-label">Beds</div><div class="field">Any<span>▾</span></div></div>
        <div><div class="field-label">Baths</div><div class="field">Any<span>▾</span></div></div>
      </div>
      <div class="search-btn">SEARCH</div>
    </div>
  </form>

  <section class="service-band"></section>
  <div class="service" style="left:233px;top:626px">
    <div class="circle"><svg width="58" height="58" viewBox="0 0 58 58" fill="none" stroke="#fff" stroke-width="3"><circle cx="29" cy="22" r="14"/><path d="M33 16h-6a3 3 0 0 0 0 6h4a3 3 0 0 1 0 6h-6M29 12v20"/><path d="M6 46h12l8 4h14l10-8"/></svg></div>
    Sell With Clearmarrow<br>&amp; Save $$$
  </div>
  <div class="service" style="left:486px;top:626px">
    <div class="circle"><svg width="58" height="58" viewBox="0 0 58 58" fill="none" stroke="#fff" stroke-width="3"><path d="M8 28L29 10l21 18M14 24v22h14"/><circle cx="37" cy="38" r="7"/><path d="M42 43l7 7"/></svg></div>
    Start Your Home<br>Search With Us
  </div>
  <div class="service" style="left:740px;top:626px">
    <div class="circle"><svg width="58" height="58" viewBox="0 0 58 58" fill="none" stroke="#fff" stroke-width="3"><path d="M18 24L30 13l12 11M22 21v12h16V21"/><path d="M6 44h12l8 4h14l10-8"/></svg></div>
    Leasing &amp; Property<br>Management
  </div>
  <div class="btn" style="left:512px;top:840px;width:176px;height:38px">CALL US TODAY</div>

  <h2 class="sec-title" style="top:988px"><b>CLEARMARROW</b> PROPERTIES</h2>

  <article class="prop" style="left:141px"><div class="photo" role="img" aria-label="Photo of a two-storey white house with garage" style="background:linear-gradient(180deg,#8fb8e0 0%,#e8ebe8 45%,#6b8a55 100%)"></div><span class="badge">Saved $4,650</span><div class="addr">4820 Willowmere Lane<br>Lake Worth, FL 33463- $310,000</div></article>
  <article class="prop" style="left:455px"><div class="photo" role="img" aria-label="Photo of a bright living room interior" style="background:linear-gradient(180deg,#d9d9d9 0%,#a8a8a8 50%,#4a4a4a 100%)"></div><span class="badge">Saved $4,650</span><div class="addr">318 Coral Vista Drive, 204<br>Boynton Beach, FL 33435 - $499,000</div></article>
  <article class="prop" style="left:770px"><div class="photo" role="img" aria-label="Photo of a cream two-storey house with garage" style="background:linear-gradient(180deg,#9cc1e4 0%,#e9dcb8 50%,#7d8a5d 100%)"></div><span class="badge">Saved $4,650</span><div class="addr">9716 Saddlebrook Circle<br>Lake Worth, FL 33449- $310,000</div></article>
  <div class="btn" style="left:511px;top:1434px;width:178px;height:38px">VIEW ALL</div>

  <section class="realtor-band">
    <div class="realtor-frame">
      <h2>Boynton Beach Realtor - Discover Some of the Best Communities in Palm Beach County, FL</h2>
      <p>Over here at Clearmarrow Realty, we have some of the best Realtors in the community who are ready to assist you and provide you with a free consultation.</p>
      <div class="btn" style="left:355px;top:112px;width:262px;height:36px">CALL TODAY! 561-555-0184</div>
    </div>
  </section>

  <h2 class="sec-title" style="top:1827px"><b>LATEST PROPERTIES</b> WE'VE SOLD</h2>
  <span class="arrow" style="left:98px">‹</span><span class="arrow" style="left:1078px">›</span>
  <article class="sold" style="left:141px"><div class="photo" role="img" aria-label="Photo of a single-storey house" style="background:linear-gradient(180deg,#8cb4da,#d9d4c4 55%,#576b45)"></div><span class="tag">SOLD</span><div class="info">715 NW 8th Street, Boynton...<br><b>$199,000</b></div><div class="meta"><span>4 Beds</span><span>2 Baths</span><span>1635 Sq Ft</span></div></article>
  <article class="sold" style="left:376px"><div class="photo" role="img" aria-label="Photo of a house with red tile roof" style="background:linear-gradient(180deg,#94bfe2,#b0523c 45%,#4f6b3a)"></div><span class="tag">SOLD</span><div class="info">3290 Palmetto Dr, Delray...<br><b>$320,000</b></div><div class="meta"><span>4 Beds</span><span>3 Baths</span><span>2013 Sq Ft</span></div></article>
  <article class="sold" style="left:611px"><div class="photo" role="img" aria-label="Photo of a house behind palm trees" style="background:linear-gradient(180deg,#a8c8e6,#cfc7b2 50%,#5d6f48)"></div><span class="tag">SOLD</span><div class="info">2612 Finch Road W, Lake Worth<br><b>$199,000</b></div><div class="meta"><span>4 Beds</span><span>2 Baths</span><span>1635 Sq Ft</span></div></article>
  <article class="sold" style="left:844px"><div class="photo" role="img" aria-label="Photo of a grey house with garage" style="background:linear-gradient(180deg,#9ebfe0,#c9cbcc 50%,#66704f)"></div><span class="tag">SOLD</span><div class="info">4471 Marigold Lane...<br><b>$199,900</b></div><div class="meta"><span>3 Beds</span><span>2 Baths</span><span>1453 Sq Ft</span></div></article>

  <section class="broker">
    <div class="broker-photo" role="img" aria-label="Black and white portrait of the broker in a suit"></div>
    <h2 class="broker-name">Marcel Dantine, Lic. Real Estate Broker</h2>
    <p class="broker-text">On average, our customers save <b>$5,600</b> when they list with us... and they still receive top marketing and quality professional service!</p>
    <div class="broker-call">Call Us Today And Save Thousands $$$</div>
    <div class="broker-web"><svg width="16" height="16" viewBox="0 0 16 16" fill="none" stroke="#333" stroke-width="1.3"><circle cx="8" cy="8" r="7"/><ellipse cx="8" cy="8" rx="3" ry="7"/><path d="M1 8h14"/></svg>www.clearmarrow.us</div>
    <div class="follow">Follow Me On : <i class="social-c"></i><i class="social-c"></i><i class="social-c"></i><i class="social-c"></i><i class="social-c"></i><i class="social-c"></i></div>
  </section>

  <h2 class="sec-title" style="top:2753px"><b>CLIENT</b> TESTIMONIALS</h2>
  <article class="testi" style="left:141px"><div class="avatar" role="img" aria-label="Client portrait"></div><div class="who">Helen, Juno</div><div class="stars">☆☆☆☆☆</div><p>Lorem Ipsum is simply dummy text of the printing and typesetting industry. Lorem Ipsum has been the industry's standard dummy text ever since the 1500s, when an unknown printer.</p></article>
  <article class="testi" style="left:458px"><div class="avatar" role="img" aria-label="Client portrait"></div><div class="who">Rita, Ocala</div><div class="stars">☆☆☆☆☆</div><p>Lorem Ipsum is simply dummy text of the printing and typesetting industry. Lorem Ipsum has been the industry's standard dummy text ever since the 1500s, when an unknown printer.</p></article>
  <article class="testi" style="left:778px"><div class="avatar" role="img" aria-label="Client portrait"></div><div class="who">Daniel, Tampa</div><div class="stars">☆☆☆☆☆</div><p>Lorem Ipsum is simply dummy text of the printing and typesetting industry. Lorem Ipsum has been the industry's standard dummy text ever since the 1500s, when an unknown printer.</p></article>
  <div class="dots"><i></i><i></i><i></i></div>

  <section class="cta">
    <div class="cta-photo" role="img" aria-label="Photo of an agent shaking hands with a client"></div>
    <h3>30 Day Listing Service Guaranteed.</h3>
    <h4>Save Thousands $$$</h4>
    <h5>LISTING WITH US!</h5>
  </section>

  <section class="contact" role="region" aria-label="Contact">
    <div class="kicker" style="left:200px;top:32px">FILL THE FORM TO CONTACT</div>
    <h2 style="left:200px;top:46px">GET IN TOUCH</h2>
    <div class="input" style="top:150px">Your Name</div>
    <div class="input" style="top:194px">Email Address</div>
    <div class="input" style="top:238px">Phone Number</div>
    <div class="input" style="top:282px;height:84px;align-items:flex-start;padding-top:10px">Your Message</div>
    <div class="send">SEND MESSAGE</div>

    <div class="kicker" style="left:727px;top:32px">CLEARMARROW OFFICE</div>
    <h2 style="left:727px;top:46px">OFFICE ADDRESS</h2>
    <div class="office" style="top:150px"><div class="ic"><svg width="12" height="16" viewBox="0 0 9 12"><path d="M4.5 0A4.5 4.5 0 0 0 0 4.5C0 8 4.5 12 4.5 12S9 8 9 4.5A4.5 4.5 0 0 0 4.5 0zm0 6.3a1.8 1.8 0 1 1 0-3.6 1.8 1.8 0 0 1 0 3.6z" fill="#fff"/></svg></div><div class="t"><b>CLEARMARROW</b>2140 Harbor Crest Blvd, Ste 310, Boynton<br>Beach, FL 33426</div></div>
    <div class="office" style="top:236px"><div class="ic"><svg width="16" height="16" viewBox="0 0 24 24"><path d="M6.6 10.8a15 15 0 0 0 6.6 6.6l2.2-2.2c.3-.3.7-.4 1-.2 1.1.4 2.3.6 3.6.6.6 0 1 .4 1 1V20c0 .6-.4 1-1 1A17 17 0 0 1 3 4c0-.6.4-1 1-1h3.5c.6 0 1 .4 1 1 0 1.3.2 2.5.6 3.6.1.3 0 .7-.2 1z" fill="#fff"/></svg></div><div class="t"><b>PHONE</b>561-555-0184</div></div>
    <div class="office" style="top:306px"><div class="ic"><svg width="16" height="16" viewBox="0 0 16 16" fill="#fff"><rect x="4" y="1" width="8" height="5"/><rect x="1" y="6" width="14" height="6" rx="1"/><rect x="4" y="10" width="8" height="5"/></svg></div><div class="t"><b>FAX</b>561-555-0127</div></div>
    <div class="office" style="top:376px"><div class="ic"><svg width="16" height="13" viewBox="0 0 20 16"><rect x="1" y="1" width="18" height="14" rx="1" fill="none" stroke="#fff" stroke-width="1.8"/><path d="M1 2l9 7 9-7" fill="none" stroke="#fff" stroke-width="1.8"/></svg></div><div class="t"><b>EMAIL</b>contact@clearmarrow.us</div></div>
  </section>

  <footer class="footer">
    <span>Copyright © 2018 Clearmarrow.us. All Rights Reserved.</span>
    <span class="socials"><i></i><i></i><i></i><i></i><i></i><i></i></span>
  </footer>
</div>
</body>
</html>
```